依頼詳細
今回は」取り急ぎ3種類の用途のメッセージカードのデザイン作成の依頼です。
メッセージカードに入れる文章も決まっていますのでその内容も入れての作成をお願いします。追加の依頼として14種類のメッセージカードの依頼もありますのでよろしくお願いします。
記載項目
株式会社マツバネ贈答
担当:田辺
TEL025-275-1277 FAX025-275-1350
Email:kenji@matsubanezoto.example.jp
希望イメージ
シンプル 複雑
単色 カラフル
暗い 明るい
日常 高級
遊び心 厳粛
未来的 伝統的
女性的 男性的
希望する色
設定なし
納品ファイル
• イラストレーター形式 (.ai)
• フォトショップ形式 (.psd)
• PNG形式 (.png)
補足説明
メッセージカードに入れる文章を添付しますので、よろしくお願いします。
また、参考までに今現在使用しているメッセージカードを添付します。
全く違うイメージでOKです。逆に異なった方がいいです。
サイズ:B7サイズ 91 × 128 ミリ
■ 選んだ理由

ご用途に合った上品なデザインが素敵でした。
年配の方への贈り物が多いので、特に還暦・長寿が派手過ぎず華やかで好感が持てました。

■ 提案者全員のお礼・コメント

たくさんのご提案をいただき、誠にありがとうございました。
どれも素敵なデザインでしたので選出にかなり迷いました。
他の用途でも依頼が出来たらと思いますので、またご縁がございましたらよろしくお願い致します。

```html
<!DOCTYPE html>
<html lang="ja">
<head>
<meta charset="utf-8">
<title>長寿祝いメッセージカード</title>
<link rel="stylesheet" href="https://fonts.googleapis.com/css2?family=Yuji+Boku&family=Yusei+Magic&display=swap">
<style>
  :root {
    --paper: #ffffff;
    --pattern-green: #3d6f58;
    --pattern-sage: #7f9a88;
    --pattern-brown: #8f7f63;
    --pattern-sand: #b9a886;
    --gold-light: #f5da55;
    --gold-mid: #e6bd2e;
    --gold-deep: #cf9a1d;
    --ink: #1a1613;
    --celebration-red: #d8232a;
  }
  html, body {
    margin: 0;
    padding: 0;
    width: 857px;
    height: 1200px;
    overflow: hidden;
    background: var(--paper);
  }
  .card {
    position: relative;
    width: 857px;
    height: 1200px;
    background: var(--paper);
  }
  .card__pattern {
    position: absolute;
    left: 129px;
    top: 186px;
    width: 600px;
    height: 894px;
    background: linear-gradient(170deg, var(--pattern-sage) 0%, var(--pattern-green) 30%, var(--pattern-brown) 55%, var(--pattern-sand) 75%, var(--pattern-green) 100%);
  }
  .card__panel {
    position: absolute;
    left: 207px;
    top: 271px;
    width: 444px;
    height: 735px;
    background: linear-gradient(135deg, var(--gold-light) 0%, var(--gold-mid) 45%, var(--gold-light) 70%, var(--gold-deep) 100%);
  }
  .card__title {
    position: absolute;
    left: 560px;
    top: 288px;
    width: 64px;
    writing-mode: vertical-rl;
    font-family: "Yuji Boku", serif;
    font-size: 62px;
    line-height: 1;
    letter-spacing: 8px;
    color: var(--ink);
    margin: 0;
    font-weight: 400;
  }
  .card__title-mark {
    color: var(--celebration-red);
  }
  .card__message {
    position: absolute;
    right: 306px;
    top: 429px;
    height: 420px;
    writing-mode: vertical-rl;
    font-family: "Yusei Magic", sans-serif;
    font-size: 24px;
    line-height: 2.6;
    color: var(--ink);
    margin: 0;
  }
</style>
</head>
<body>
  <div class="card">
    <div class="card__pattern" role="img" aria-label="緑と茶色の和柄（青海波・亀甲など）の背景模様"></div>
    <div class="card__panel" role="img" aria-label="金箔風のきらめく金色の台紙"></div>
    <h1 class="card__title"><span class="card__title-mark">祝</span>長寿</h1>
    <p class="card__message">謹んで長寿のお祝いを申し上げます。<br>これからもお体を大切に、<br>いつまでもお元気でいてください。</p>
  </div>
</body>
</html>
```